vantoreq realty business card

We need a Business card for our new business. The logo was designed by BrushQuill, and the text We want on the back is:
REAL ESTATE INVESTMENTS
- BUY, RENOVATE, SELL AND RENT RESIDENTIAL PROPERTIES
- FULL HOME REHABBING , REMODELING AND INTERIOR DESIGN
- HOME STAGING SERVICES
- WHOLESALE INVESTOR PROPERTIES
- MAKE CASH OFFERS ON HOUSES IN ANY CONDITION AND IN ANY SITUATION
- PRIVATE MONEY INVESTOR PROGRAMS WITH 6-12% RETURNS
- PAY CASH REWARDS FOR REFFERALS
- CONCIERGE SERVICE

Business

```html
<!DOCTYPE html>
<html lang="en">
<head>
<meta charset="utf-8">
<title>Vantoreq Realty – Business Card</title>
<link rel="stylesheet" href="https://fonts.googleapis.com/css2?family=Open+Sans:wdth,wght@75..100,400..700&display=swap">
<style>
  :root {
    --brand-blue: #73c8dc;
    --brand-grey: #8b8c8e;
    --text-grey: #7a7b7d;
    --card-white: #ffffff;
    --page-bg: #ecebea;
    --card-shadow: 0 4px 14px rgba(0, 0, 0, 0.18);
  }
  html, body {
    margin: 0;
    padding: 0;
    overflow: hidden;
    background: var(--page-bg);
  }
  .canvas {
    position: relative;
    width: 1200px;
    height: 1000px;
    overflow: hidden;
    background: var(--page-bg);
    font-family: "Open Sans", Arial, sans-serif;
  }
  .card {
    position: absolute;
    left: 265px;
    width: 666px;
    height: 397px;
    background: var(--card-white);
    box-shadow: var(--card-shadow);
    overflow: hidden;
  }
  .card--front { top: 73px; }
  .card--back { top: 533px; }

  .band {
    position: absolute;
    bottom: 0;
    height: 32px;
  }
  .band--grey { left: 0; width: 330px; background: var(--brand-grey); }
  .band--blue { left: 335px; right: 0; background: var(--brand-blue); }

  .brand-mark {
    position: absolute;
    background: var(--brand-blue);
  }
  .brand-name {
    position: absolute;
    margin: 0;
    color: var(--brand-blue);
    font-weight: 400;
    letter-spacing: 0.5px;
    white-space: nowrap;
  }
  .brand-tagline {
    position: absolute;
    margin: 0;
    color: var(--text-grey);
    letter-spacing: 1.5px;
    white-space: nowrap;
  }

  /* front */
  .card--front .brand-mark { left: 33px; top: 69px; width: 58px; height: 72px; }
  .card--front .brand-name { left: 124px; top: 68px; font-size: 37px; line-height: 44px; }
  .card--front .brand-tagline { left: 125px; top: 122px; font-size: 19px; line-height: 24px; }

  .person { position: absolute; left: 33px; top: 218px; margin: 0; }
  .person__name {
    display: block;
    color: var(--brand-blue);
    font-size: 27px;
    font-weight: 700;
    line-height: 34px;
  }
  .person__role {
    display: block;
    color: var(--text-grey);
    font-size: 17px;
    line-height: 20px;
  }
  .website {
    position: absolute;
    left: 33px;
    top: 328px;
    margin: 0;
    color: var(--brand-blue);
    font-size: 17px;
    font-weight: 700;
  }
  .contact {
    position: absolute;
    left: 333px;
    top: 220px;
    margin: 0;
    font-size: 17px;
    line-height: 22.5px;
    color: var(--text-grey);
    font-style: normal;
  }
  .contact__label { color: var(--brand-blue); font-weight: 700; }
  .contact__address { display: block; margin-top: 18px; }

  /* back */
  .card--back .brand-mark { left: 302px; top: 22px; width: 62px; height: 74px; }
  .card--back .brand-name {
    left: 0; right: 0; top: 112px; text-align: center;
    font-size: 28px; line-height: 34px;
  }
  .card--back .brand-tagline {
    left: 0; right: 0; top: 150px; text-align: center;
    font-size: 14px; line-height: 18px;
  }
  .services {
    position: absolute;
    left: 0;
    right: 0;
    top: 183px;
    margin: 0;
    padding: 0;
    list-style: none;
    text-align: center;
    color: var(--text-grey);
    font-size: 15px;
    font-weight: 600;
    font-stretch: 78%;
    line-height: 20.9px;
    letter-spacing: 0.2px;
  }
</style>
</head>
<body>
<div class="canvas">

  <section class="card card--front" aria-label="Business card front">
    <span class="brand-mark" aria-hidden="true"></span>
    <h1 class="brand-name">VANTOREQ Realty</h1>
    <p class="brand-tagline">REAL ESTATE SOLUTIONS</p>

    <p class="person">
      <span class="person__name">Dana R Holt</span>
      <span class="person__role">Manager</span>
    </p>
    <p class="website">www.vantoreqrealty.com</p>

    <address class="contact">
      <span class="contact__label">Phone:</span> + 999 999 9999<br>
      <span class="contact__label">Fax:</span> + 999 999 9999<br>
      <span class="contact__label">Email:</span> dana@vantoreqrealty.com
      <span class="contact__address">42 Alder Lane, Brookfield<br>Oakshire, OK4</span>
    </address>

    <div class="band band--grey"></div>
    <div class="band band--blue"></div>
  </section>

  <section class="card card--back" aria-label="Business card back">
    <span class="brand-mark" aria-hidden="true"></span>
    <h2 class="brand-name">VANTOREQ Realty</h2>
    <p class="brand-tagline">REAL ESTATE SOLUTIONS</p>

    <ul class="services">
      <li>- BUY, RENOVATE, SELL AND RENT RESIDENTIAL PROPERTIES -</li>
      <li>- FULL HOME REHABBING , REMODELING AND INTERIOR DESIGN -</li>
      <li>- HOME STAGING SERVICES -</li>
      <li>- WHOLESALE INVESTOR PROPERTIES -</li>
      <li>- MAKE CASH OFFERS ON HOUSES IN ANY CONDITION AND IN ANY SITUATION -</li>
      <li>- PRIVATE MONEY INVESTOR PROGRAMS WITH 6-12% RETURNS -</li>
      <li>- PAY CASH REWARDS FOR REFFERALS -</li>
      <li>- CONCIERGE SERVICE -</li>
    </ul>

    <div class="band band--grey"></div>
    <div class="band band--blue"></div>
  </section>

</div>
</body>
</html>
```